Business cards and letterhead
Business cards and letterhead - Pharmacy/Pharmaceuticals
Creative Brief
Professional
Owen Lilcroft
Partner
4178 Heron Lake Road Suite 410 Grapevine, TX 76099
owen@torvalepz.com
torvalepz.com

```html
<!DOCTYPE html>
<html lang="en">
<head>
<meta charset="utf-8">
<title>Torvale Business Card</title>
<link href="https://fonts.googleapis.com/css2?family=Open+Sans:wght@400;600;800&display=swap" rel="stylesheet">
<style>
  :root {
    --page: #e9e8e6;
    --blue-deep: #1b57bf;
    --blue-light: #4a9af0;
    --grey: #898c91;
    --grey-dark: #6f7276;
    --white: #ffffff;
    --brand: #1e62c9;
  }
  html, body { margin: 0; padding: 0; overflow: hidden; }
  body {
    width: 1200px; height: 803px;
    background: var(--page);
    font-family: "Open Sans", Arial, sans-serif;
    position: relative;
  }
  .card {
    position: absolute;
    top: 246px;
    width: 540px; height: 310px;
    overflow: hidden;
    box-shadow: 0 6px 18px rgba(0,0,0,.18);
  }
  .card--front { left: 45px; }
  .card--back { left: 615px; }
  .card__art { position: absolute; inset: 0; }
  .brand {
    position: absolute; left: 250px; top: 54px;
    display: flex; align-items: center; gap: 10px;
  }
  .brand__dot { width: 36px; height: 36px; border-radius: 50%; background: var(--brand); }
  .brand__name { font-weight: 800; font-size: 34px; color: var(--brand); line-height: 1; }
  .brand__tag {
    position: absolute; left: 344px; top: 96px;
    font-size: 9px; font-weight: 600; color: var(--brand); letter-spacing: 1px; text-transform: uppercase;
  }
  .contact { position: absolute; color: var(--white); font-size: 11px; line-height: 1.45; }
  .contact svg { position: absolute; left: -20px; top: 2px; }
  .contact--phone { left: 38px; top: 130px; }
  .contact--address { left: 38px; top: 176px; width: 180px; font-size: 10px; }
  .web-pill {
    position: absolute; left: 300px; top: 160px;
    width: 222px; height: 32px; border-radius: 16px;
    background: var(--grey-dark); color: var(--white);
    font-size: 12px; line-height: 32px; text-align: center;
  }
  .contact--email { left: 330px; top: 260px; font-size: 13px; }
  .contact--email svg { left: -28px; top: 1px; }
  .person {
    position: absolute; right: 34px; top: 30px;
    color: var(--white); text-align: right;
  }
  .person__name { font-size: 18px; font-weight: 600; text-transform: uppercase; letter-spacing: 1px; }
  .person__role { font-size: 11px; opacity: .9; }
</style>
</head>
<body>

<section class="card card--front" aria-label="Card front">
  <svg class="card__art" width="540" height="310" viewBox="0 0 540 310">
    <defs>
      <linearGradient id="frontBlue" x1="0" y1="0" x2="1" y2="1">
        <stop offset="0" stop-color="var(--blue-light)"/>
        <stop offset="1" stop-color="var(--blue-deep)"/>
      </linearGradient>
    </defs>
    <rect width="540" height="310" fill="url(#frontBlue)"/>
    <rect width="540" height="42" fill="var(--grey)"/>
    <path d="M0 42 H540 V208 H306 Q288 208 282 192 L268 128 Q262 110 242 110 H0 Z" fill="var(--white)"/>
  </svg>

  <div class="brand"><span class="brand__dot"></span><span class="brand__name">Torvale</span></div>
  <div class="brand__tag">Pharma Solutions</div>

  <div class="contact contact--phone">
    <svg width="12" height="14" viewBox="0 0 12 14"><path d="M2 1 L5 1 L6 4 L4 5 Q5 8 7 10 L8 8 L11 9 L11 12 Q6 13 3 8 Q1 5 2 1 Z" fill="var(--white)"/></svg>
    014 552 8731<br>014 552 8732
  </div>
  <div class="contact contact--address">
    <svg width="13" height="12" viewBox="0 0 13 12"><path d="M6.5 0 L13 6 H11 V12 H2 V6 H0 Z" fill="var(--white)"/></svg>
    4178 Heron Lake Road Suite 410<br>Grapevine, TX 76099
  </div>

  <div class="web-pill">www.torvalepz.com</div>

  <div class="contact contact--email">
    <svg width="20" height="14" viewBox="0 0 20 14"><rect x=".5" y=".5" width="19" height="13" fill="none" stroke="var(--white)"/><path d="M.5 .5 L10 8 L19.5 .5" fill="none" stroke="var(--white)"/></svg>
    owen@torvalepz.com
  </div>
</section>

<section class="card card--back" aria-label="Card back">
  <svg class="card__art" width="540" height="310" viewBox="0 0 540 310">
    <defs>
      <linearGradient id="backBlue" x1="0" y1="0" x2="1" y2="1">
        <stop offset="0" stop-color="var(--blue-light)"/>
        <stop offset="1" stop-color="var(--blue-deep)"/>
      </linearGradient>
    </defs>
    <rect width="540" height="310" fill="var(--grey)"/>
    <path d="M0 0 H540 V150 H0 Z" fill="url(#backBlue)"/>
    <path d="M0 150 H540 V190 H410 Q392 190 386 204 L378 222 Q372 236 354 236 H250 Q232 236 226 222 L218 204 Q212 190 194 190 H0 Z" fill="var(--white)"/>
  </svg>
  <div class="person">
    <div class="person__name">Owen Lilcroft</div>
    <div class="person__role">Partner</div>
  </div>
</section>

</body>
</html>
```